Velora Botanics- New and unique line of Pet Products

Hi,

Velora Botanics is a manufacturer of natural products.

We need fresh and creative labels, for our new pet care product line:
- Specially scented for male- dog shampoo called "Ranger"
- Specially scented for female- dog shampoo called "Velvet paws"
- Cat cleaning wipes
- Stain and odor remover (for pet urine)

For more info on the products:
Velorabotanics.com
(please don't rely on the current labels for the pet products)

ATTACHED- you will find 2 products from Shopvale, which we like the design, as an example.

Best wishes,
Tomas
Velora Botanicsâ„¢
Updates

Project Deadline Extended
Reason: I did a vote, No one is very excited about the current designs Im not sure what to do next
Added Wednesday, August 24, 2016

Target Market(s)

Designed for pet owners and pet grooming professionals.

Industry/Entity Type

Pet Care

Requirements
Must have
• - The label should have a common language between products; same them, that can be modified to all products by change of writing and picture.
• - Reflects the natural aspect of the company & products, safe for the children and pets, was NOT tested on animals
• - Unique feature of the product (one destined for male dogs, other for female, the third for cats)
• Attached company Logo (Velora Botanicsâ„¢); should appear on the label.
• - Emphasize the difference for male / female dogs.
Nice to have
• - Maybe cartoon of a family bathing the male dog / female dog / cat - ?
• I think that the common feature should be a cartoon of a pet owner/s with different pets
• Made in the USA
• - Bottles are white
• - Dimensions:
• Male dog / Female dog / Odor & stain - 6"x7" & 4.25"x11"
• Cat: 4.5"x2.5" front & back
Should not have
• Please don't use stock images;
• We do private label and cannot have similar photos as our customers, must be unique.

```html
<!DOCTYPE html>
<html lang="en">
<head>
<meta charset="utf-8">
<title>Ranger Oatmeal Dog Shampoo Label</title>
<link rel="stylesheet" href="https://fonts.googleapis.com/css2?family=Poppins:wght@600;800;900&family=Comfortaa:wght@500&family=Nunito:wght@400&display=swap">
<style>
  :root {
    --navy: #283f87;
    --sun: #ecb624;
    --leaf: #a5c95b;
    --white: #ffffff;
    --ink: #2b3c8a;
    --grey: #8a8f94;
    --tub: #e2a92a;
    --fur: #d9cdb0;
  }
  * { margin: 0; padding: 0; box-sizing: border-box; }
  html, body { width: 767px; height: 1200px; overflow: hidden; background: var(--navy); }
  .label { position: relative; width: 767px; height: 1200px; overflow: hidden; background: var(--navy); }
  .shapes { position: absolute; inset: 0; }
  .brand {
    position: absolute; top: 64px; left: 0; width: 767px;
    display: flex; justify-content: center; align-items: center; gap: 10px;
    font-family: "Nunito", sans-serif; font-weight: 400; font-size: 27px;
    color: var(--grey); letter-spacing: 0.5px;
  }
  .brand-dot { width: 16px; height: 16px; border-radius: 50%; background: var(--leaf); }
  .product-name {
    position: absolute; top: 170px; left: 258px;
    font-family: "Poppins", sans-serif; font-weight: 800; font-size: 132px;
    line-height: 1; color: var(--white); letter-spacing: -2px;
  }
  .product-type {
    position: absolute; top: 372px; left: 0; width: 767px; text-align: center;
    font-family: "Poppins", sans-serif; font-weight: 800; font-size: 40px;
    color: var(--white);
  }
  .ingredients {
    position: absolute; top: 428px; left: 0; width: 767px; text-align: center;
    font-family: "Poppins", sans-serif; font-weight: 800; font-size: 24px;
    color: var(--white);
  }
  .illustration {
    position: absolute; left: 160px; top: 460px; width: 450px; height: 430px;
    border-radius: 40px 40px 30px 30px;
    background: linear-gradient(180deg, var(--fur) 0%, var(--fur) 45%, var(--tub) 62%, var(--tub) 100%);
  }
  .benefits {
    position: absolute; top: 900px; left: 0; width: 767px; list-style: none;
    font-family: "Comfortaa", sans-serif; font-weight: 500; font-size: 34px;
    color: var(--ink); line-height: 40px; text-align: center;
    transform: rotate(-4deg);
  }
  .benefits li::before { content: "· "; }
  .net-contents {
    position: absolute; top: 1128px; left: 0; width: 767px; text-align: center;
    font-family: "Poppins", sans-serif; font-weight: 800; font-size: 26px;
    color: var(--white);
  }
</style>
</head>
<body>
<main class="label">
  <svg class="shapes" width="767" height="1200" viewBox="0 0 767 1200" aria-hidden="true">
    <polygon class="band-sun" points="0,87 767,133 767,313 0,367" fill="var(--sun)"/>
    <path class="brand-cloud" d="M187,0 H640 C650,60 620,120 560,132 C500,142 470,112 420,128 C360,146 300,138 260,118 C210,96 190,60 187,0 Z" fill="var(--white)"/>
    <polygon class="band-leaf" points="0,854 767,754 767,1100 0,1100" fill="var(--leaf)"/>
    <g class="bubbles" fill="var(--white)">
      <circle cx="189" cy="545" r="26"/>
      <circle cx="52" cy="605" r="34"/>
      <circle cx="122" cy="670" r="11"/>
      <circle cx="646" cy="500" r="22"/>
      <circle cx="592" cy="551" r="13"/>
      <circle cx="696" cy="627" r="46"/>
    </g>
    <circle class="name-mark" cx="133" cy="247" r="58" fill="var(--white)"/>
  </svg>

  <div class="brand"><span class="brand-dot"></span>Velora Botanics</div>

  <h1 class="product-name">ranger</h1>
  <p class="product-type">Oatmeal Dog Shampoo</p>
  <p class="ingredients">Aloe Vera • Chamoline extract • Vitamin E</p>

  <div class="illustration" role="img" aria-label="Cartoon of a happy shaggy dog with foam on its head sitting in a yellow bathtub full of suds"></div>

  <ul class="benefits">
    <li>Super concentrated</li>
    <li>Deodorizing</li>
    <li>PH balanced</li>
    <li>Pure and natural</li>
  </ul>

  <p class="net-contents">Net Contents 16 fl. oz (472 ml)</p>
</main>
</body>
</html>
```